Business Card design for an International Import Export House

We need a Business Card design for our import export business. We trade in Minerals, Metals, Rice, Sugar, Steel etc.. The design should be minimalistic. It may or may not contain the physical address. In case you want to include the physical address - 418 Verandah Heights, Marlow Sector 9, Gurgaon, Haryana, India, 122009.

Target Market(s)

Steel Mills or Steel Plants, Factories, Mining businesses, Industrial houses, Government Agencies

Industry/Entity Type

Importer

Contact Information for Business Card

Business Name - Varndell Overseas

Font styles to use
Other font styles liked:
• montserrat

Requirements
Must have
• Ravi Kandola - President
• www.varndelloverseas.com
• ravi@varndelloverseas.com
• +91-987-654-3217
Nice to have
• worldwide suppliers of ores

```html
<!DOCTYPE html>
<html lang="en">
<head>
<meta charset="utf-8">
<title>Varndell Overseas — Business Card</title>
<link rel="stylesheet" href="https://fonts.googleapis.com/css2?family=Montserrat:wght@500;600&family=Lato:wght@400&display=swap">
<style>
  :root {
    --backdrop: #2a2a2b;
    --card: #141517;
    --card-edge: #1c1d20;
    --teal: #3f8fae;
    --white: #f2f2f2;
    --muted: #d4d6d8;
  }
  html, body {
    margin: 0;
    width: 1200px;
    height: 716px;
    overflow: hidden;
    background: var(--backdrop);
  }
  .canvas {
    position: relative;
    width: 1200px;
    height: 716px;
  }
  .card {
    position: absolute;
    top: 215px;
    width: 500px;
    height: 286px;
    background: var(--card);
    border: 1px solid var(--card-edge);
    border-radius: 6px;
    box-shadow: 0 14px 30px rgba(0,0,0,0.45);
    overflow: hidden;
  }
  .card--front { left: 70px; }
  .card--back { left: 630px; }

  .brand {
    position: absolute;
    left: 40px;
    top: 70px;
    display: flex;
    align-items: center;
    gap: 10px;
  }
  .brand__dot {
    width: 14px;
    height: 14px;
    border-radius: 50%;
    background: var(--teal);
  }
  .brand__name {
    font-family: "Montserrat", sans-serif;
    font-weight: 600;
    font-size: 16px;
    color: var(--teal);
    text-transform: uppercase;
    white-space: nowrap;
  }
  .divider {
    position: absolute;
    left: 40px;
    right: 40px;
    top: 150px;
    height: 1px;
    background: var(--teal);
  }
  .contact {
    position: absolute;
    left: 40px;
    top: 164px;
    font-family: "Lato", sans-serif;
    font-size: 12.5px;
    line-height: 18px;
    color: var(--muted);
  }
  .holder__name {
    position: absolute;
    right: 40px;
    top: 124px;
    font-family: "Montserrat", sans-serif;
    font-weight: 500;
    font-size: 17px;
    color: var(--teal);
    text-transform: uppercase;
    white-space: nowrap;
  }
  .holder__title {
    position: absolute;
    right: 40px;
    top: 157px;
    font-family: "Lato", sans-serif;
    font-size: 13px;
    color: var(--white);
  }
  .corner-mark {
    position: absolute;
    right: 0;
    top: 160px;
  }

  .back-name {
    position: absolute;
    right: 42px;
    bottom: 40px;
    font-family: "Montserrat", sans-serif;
    font-weight: 600;
    font-size: 22px;
    color: var(--white);
    text-transform: uppercase;
    white-space: nowrap;
  }
</style>
</head>
<body>
<main class="canvas">
  <section class="card card--front" aria-label="Card front">
    <div class="brand">
      <span class="brand__dot"></span>
      <span class="brand__name">Varndell Overseas</span>
    </div>
    <div class="holder__name">Ravi Kandola</div>
    <div class="divider"></div>
    <div class="holder__title">President</div>
    <div class="contact">
      <div>+91-987-654-3217</div>
      <div>ravi@varndelloverseas.com</div>
      <div>www.varndelloverseas.com</div>
    </div>
    <svg class="corner-mark" width="14" height="22" viewBox="0 0 14 22" aria-hidden="true">
      <polygon points="14,0 14,22 0,22" fill="var(--teal)"/>
      <polygon points="14,8 14,22 5,22" fill="var(--white)"/>
    </svg>
  </section>

  <section class="card card--back" aria-label="Card back">
    <div class="back-name">Varndell Overseas</div>
  </section>
</main>
</body>
</html>
```